Veterinary TPLO Surgery Flyer Design

Please use this flyer to make a professional-looking 1 page, double-sided client handout regarding TPLO.

You can visit our website at www.brackenfieldpetcare.com & www.northwoodsanimalsurgerygroup.com for additional logo information. The flyer should include all the text from the one provided.

Target Market(s)

Client communication to for referral surgery between sister veterinary clinics

Industry/Entity Type

Veterinary

Requirements
Must have
• The text included
Nice to have
• Nice to have the Cedar Hollow Avenue Animal CLinic & Dr. Pell Mobile vet logos incorporated.

```html
<!DOCTYPE html>
<html lang="en">
<head>
<meta charset="utf-8">
<title>TPLO Surgery Client Handout</title>
<link rel="stylesheet" href="https://fonts.googleapis.com/css2?family=Montserrat:wght@300;400;600;700;800&display=swap">
<style>
:root{
  --backdrop:#d3d3d3;
  --tan:#9c8c6c;
  --sage:#5d7d68;
  --forest:#3e6b2a;
  --navy:#27357a;
  --sky:#7cc3ea;
  --ink:#222;
  --white:#fff;
  --placeholder-dark:#222;
}
*{margin:0;padding:0;box-sizing:border-box}
html,body{width:740px;height:1200px;overflow:hidden}
body{background:var(--backdrop);font-family:"Montserrat",sans-serif;position:relative;color:var(--ink)}
.page{position:absolute;left:178px;width:385px;height:542px;overflow:hidden;box-shadow:4px 5px 9px rgba(0,0,0,.35)}
.page--front{top:42px;background:var(--sage);color:var(--white)}
.page--back{top:618px;background:var(--white)}
.page-bg{position:absolute;inset:0}
.abs{position:absolute}
.brand{left:25px;top:31px;display:flex;align-items:center;gap:6px;color:var(--white);font-weight:400;font-size:15px;line-height:1.1}
.brand__mark{width:14px;height:14px;background:var(--white);border-radius:50%;flex:none}
.headline{left:25px;top:99px;width:330px;font-weight:800;font-size:7.6px;line-height:1.4}
.section-title{font-weight:600;font-size:8.5px}
.body-copy{font-weight:300;font-size:5.8px;line-height:7.7px}
.body-copy p+p{margin-top:7px}
.photo{background:linear-gradient(135deg,#c9c7c0,#e8e4d8 50%,#a9a8a6)}
.xray{background:linear-gradient(90deg,#111,#4a4a4a 45%,#1a1a1a 55%,#6a6a6a 75%,#111)}
.benefits{left:25px;top:394px;width:345px;list-style:none}
.benefits li{position:relative;padding-left:18px;margin-bottom:6px}
.benefits li::before{content:"•";position:absolute;left:0}
.benefits b,.steps b{font-weight:600}
.back-title{left:31px;top:44px;width:200px;font-weight:700;font-size:8.4px;line-height:1.3}
.badge{left:273px;top:24px;width:85px;height:82px;display:flex;flex-direction:column;align-items:center;justify-content:center;gap:5px}
.badge__circle{width:26px;height:26px;border-radius:50%;background:var(--forest)}
.badge__name{font-weight:700;font-size:8.4px;color:var(--navy)}
.bar{left:0;background:var(--forest);color:var(--white);padding-left:31px}
.bar--process{top:131px;width:133px;height:19px;font-weight:600;font-size:8.5px;line-height:19px}
.bar--post{top:337px;width:206px;height:20px;padding-top:2px}
.bar--post .section-title{font-size:8.5px;line-height:9px;display:block}
.bar--post small{font-weight:300;font-size:5.8px;display:block}
.steps{left:46px;top:157px;width:300px;list-style:none}
.steps li{margin-bottom:5.5px}
.steps li.gap{margin-bottom:12px}
.post-list{left:40px;top:364px;width:320px;list-style:none}
.post-list li{position:relative;padding-left:7px;margin-bottom:5px}
.post-list li::before{content:"•";position:absolute;left:0}
.footer{left:0;top:434px;width:385px;height:108px;background:linear-gradient(90deg,var(--navy) 0%,var(--navy) 83%,var(--sky) 100%);color:var(--white)}
.contact{position:absolute;top:31px;width:180px}
.contact h3{font-weight:600;font-size:5.8px;line-height:7.7px;margin-bottom:16px}
</style>
</head>
<body>

<section class="page page--front">
  <svg class="page-bg" width="385" height="542" viewBox="0 0 385 542" aria-hidden="true">
    <polygon points="0,0 378,0 339,139 385,139 385,330 0,362" fill="var(--tan)"/>
    <polygon points="378,0 385,0 344,139 339,139" fill="var(--white)"/>
    <polygon points="0,362 385,330 385,333 0,366" fill="var(--white)"/>
  </svg>

  <div class="abs brand"><span class="brand__mark"></span><span>Cedar Hollow Avenue<br>Animal Clinic</span></div>

  <h1 class="abs headline">Advanced Orthopedic Care by Dr. Renata Pell, DVM, DNCVS-sa<br>TPLO Surgery at Cedar Hollow Avenue Animal Clinic</h1>

  <h2 class="abs section-title" style="left:25px;top:141px">About Dr. Renata Pell</h2>
  <div class="abs body-copy" style="left:25px;top:160px;width:195px">
    <p>Dr. Renata Pell is a board-certified veterinary surgeon (Diplomate of the National College of Veterinary Surgeons) with over 18 years of experience in small animal surgery. A graduate of Great Lakes State University, she completed her surgical residency at Harborview School of Veterinary Medicine. Through her mobile practice, Northwoods Mobile Surgery, Dr. Pell now provides advanced surgical procedures—such as TPLO—directly at local clinics.</p>
  </div>
  <div class="abs photo" style="left:242px;top:143px;width:118px;height:103px" role="img" aria-label="Anatomical illustration of a canine stifle joint before and after TPLO"></div>

  <h2 class="abs section-title" style="left:25px;top:253px">What is TPLO Surgery?</h2>
  <div class="abs body-copy" style="left:25px;top:274px;width:200px">
    <p>Tibial Plateau Leveling Osteotomy (TPLO) is a surgical procedure that stabilizes the stifle (knee) joint following a cranial cruciate ligament (CCL) rupture—a common orthopedic injury in dogs. The procedure involves altering the angle of the tibial plateau to eliminate abnormal joint motion, restoring stability and improving function.</p>
  </div>
  <div class="abs xray" style="left:242px;top:255px;width:118px;height:93px" role="img" aria-label="Pre-operative and post-operative TPLO radiographs of a canine tibia"></div>

  <h2 class="abs section-title" style="left:25px;top:375px">Benefits of TPLO Surgery</h2>
  <ul class="abs benefits body-copy">
    <li><b>Enhanced Joint Stability:</b> Restores natural biomechanics, reducing pain and improving mobility.</li>
    <li><b>Faster Recovery:</b> Many dogs return to normal activity faster compared to other surgical techniques.</li>
    <li><b>Proven Long-Term Success:</b> TPLO is particularly effective in large and active breeds.</li>
  </ul>

  <h2 class="abs section-title" style="left:25px;top:453px">Why Choose Cedar Hollow Avenue Animal Clinic?</h2>
  <div class="abs body-copy" style="left:25px;top:471px;width:345px">
    <p>Partnering with Dr. Pell, Cedar Hollow Avenue Animal Clinic offers advanced orthopedic surgery on-site—eliminating the need for referrals or travel. This collaboration ensures your pet receives expert surgical care in a familiar, trusted environment.</p>
    <p>Our clinic works directly with your primary veterinarian to share medical records, diagnostics, and prescriptions, ensuring seamless and coordinated care for your pet.</p>
  </div>
</section>

<section class="page page--back">
  <svg class="page-bg" width="385" height="542" viewBox="0 0 385 542" aria-hidden="true">
    <polygon points="0,0 385,0 260,10 200,32 185,18 0,10" fill="var(--forest)"/>
  </svg>

  <h2 class="abs back-title">Diagnostic Radiographs vs. TPLO Planning Radiographs</h2>
  <div class="abs body-copy" style="left:31px;top:74px;width:195px">
    <p>While diagnostic radiographs may confirm a CCL tear, they are not sufficient for surgical planning. TPLO requires three advanced technique radiographic views with precise measurements, which must be performed under sedation to reduce discomfort and allow accurate positioning.</p>
  </div>

  <div class="abs badge"><span class="badge__circle"></span><span class="badge__name">Renata Pell</span></div>

  <h2 class="abs bar bar--process">Expected Process</h2>
  <ol class="abs steps body-copy">
    <li><b>1. Diagnosis:</b> Your pet is diagnosed with stifle instability (CCL tear) by your veterinarian.</li>
    <li><b>2. Referral:</b> Your veterinarian contacts the surgical coordinator at Cedar Hollow Avenue Animal Clinic.</li>
    <li><b>3. Consultation:</b> The coordinator contacts you to schedule a 1-hour consultation to review the procedure, estimated costs, and available surgery dates.</li>
    <li><b>4. Planning Radiographs:</b> These specialized X-rays are typically taken during the consultation under light sedation.</li>
    <li><b>5. Surgical Review:</b> Dr. Pell reviews the radiographs and your pet's medical history to confirm candidacy for TPLO.</li>
    <li class="gap"><b>6. Deposit:</b> A $3,500 deposit secures Dr. Pell's travel and surgery date. This is refundable if canceled at least 5 days prior to the scheduled procedure.</li>
    <li><b>7. Surgery Day:</b> Your pet is dropped off in the morning and surgery is performed the same day.</li>
    <li><b>8. Discharge:</b> You'll receive a post-surgery update and your pet will go home that evening.</li>
  </ol>

  <div class="abs bar bar--post">
    <span class="section-title">Post-Operative Care &amp; Follow-Up</span>
    <small>Two follow-up appointments will be scheduled:</small>
  </div>
  <ul class="abs post-list body-copy">
    <li>4 Weeks Post-Op: Evaluate healing, refill medications, and address any questions.</li>
    <li>8 Weeks Post-Op: Sedated radiographs will confirm proper healing of the surgical site and tibia.</li>
  </ul>
  <div class="abs body-copy" style="left:31px;top:394px;width:325px">
    <p>Dr. Pell will stay in direct contact with you during your pet's recovery using her custom mobile app, which allows for secure messaging and provides detailed post-operative instructions.</p>
  </div>

  <footer class="abs footer body-copy">
    <div class="contact" style="left:31px">
      <h3>Contact Information:<br>Cedar Hollow Avenue Animal Clinic</h3>
      <p>2280 Cedar Hollow Avenue, Brackenfield, MI 48917<br>(517) 555-0142<br>info@brackenfieldpetcare.com<br>www.brackenfieldpetcare.com</p>
    </div>
    <div class="contact" style="left:212px">
      <h3>Northwoods Mobile Surgery<br>(Dr. Renata Pell)</h3>
      <p>(810) 555-0187<br>drpell@northwoodssurgery.com<br>www.northwoodsanimalsurgerygroup.com</p>
    </div>
  </footer>
</section>

</body>
</html>
```